Luxurious Product label and box for all natural skincare product. + 30AUD tip to winner.

What I require.
1.     One product label and one-box design.
2.     I must have a mock-up of the bottle with the attached label and the box.
 
I have supplied the following files for the designers to use.
1.     Brand logo file. (logo.zip)
2.     Slogan file. (slogan.psd)
3.     Slogan script file. (italianno.regular.ttf)
4.     Bottle image file. (60ml_moisturiser_bottle.png)
5.     Icon bar file. (Icon_bar_en.zip)
 
Label and box Design
I am interested in your unique design concepts and colors, so please feel free to be creative.
1.     Brand name: Quenra
2.     You can use your own choice of colors in your design. I would prefer two colors (excluding logo and slogan colors), although more colors are acceptable for the right design.
3.     Label and box to have a background color or pattern.
4.     I would like the icon bar to wrap around the bottom of the label and box, covering the full width of all sides of the box.
5.     The height of the icon bar should be about 7mm to 10mm high.   
6.     The hex code for the icon bar color is #EDD6D4. The color of the icons can be any color the designer chooses.
7.     The positioning of the icons are as follows.
a)     The front panel has three icons. From left to right, they are; 100% Vegan, Product of Australia, and 100% Natural.
b)     The left side panel has three icons. From the front of the label/box to the back of the label/box, they are; Cruelty-Free, Ethical & Sustainable, and Please Recycle.
c)     The right side panel has only one icon situated at the front of the right side of the label/box. The icon is 6 Months Once Open.
 
Label.
1.     The label will be a three-panel label.
2.     The label will contain text in all three panels; however, only the text for the front panel of the label is supplied in this brief. For now, use Lorem Ipsum placeholder text to fill spaces.
3.     The final text will be provided to the winning designer so they can apply the text to the left and right panels of the label.
4.     Label size. Width 104mm x Height 83mm.
5.     The final design file must include bleed and cut lines.
 
Box.
1.     The box will contain text on all four sides; however, only the text for the front of the box is supplied in this brief. For now, use Lorem Ipsum placeholder text to fill spaces.
2.     The final text will be provided to the winning designer so they can apply the text to the left and right sides and the back of the box.
3.     The box size is 40mm wide x 40mm deep x 140mm high.
4.     The final design file must include bleed and cut lines.
 
Front Panel wording.
1.     Logo.
2.     Slogan.
3.     Moisturiser.
4.     Hydrate & Nourish.
5.     Hyaluronic Acid, Desert Lime & Green Tea.
6.     All Skin Types - Dry – Dehydrated.
7.     Icon bar.
8.     60mL
 
Bottle size
60ml White Bottle – 13.5cm High x 3.5cm Wide.

Target Market(s)

Beauty-minded Asian consumers between the age of 32 and 75 who take a proactive approach in maintaining younger-looking skin. Those who already know the danger of damaged skin caused by skincare containing harsh chemicals, and therefore choose effective natural/organic solutions to meet their skincare needs. Those who wish a more radiant glow and youthful appearance to their skin. Usually, a two-income middle to high-income bracket couple with a mindset for health and beauty.

Industry/Entity Type

Beauty and skincare.

Font styles to use
Other font styles liked:
• Logo and slogan script supplied. Designer to choose all other font or script.

Colors

Designer to choose colors to be used in the design.

Requirements
Must have
• A mock-up label on the bottle and a mock-up box. My logo and slogan are already designed with my chosen font and color.
Nice to have
• I like soft pastel colors with perhaps a small amount of stronger color.

```html
<!DOCTYPE html>
<html lang="en">
<head>
<meta charset="utf-8">
<title>Quenra Moisturiser – Label and Box</title>
<link rel="stylesheet" href="https://fonts.googleapis.com/css2?family=Barlow+Condensed:wght@400;500;600&family=Libre+Franklin:wght@400;600;800&family=Montserrat:wght@400;600&display=swap">
<style>
:root{
  --ink:#4d4c4e;
  --bar:#4f4f51;
  --frame:#646566;
  --pink:#f1d3d0;
  --blush:#f3dcd6;
  --sky:#dde4e7;
  --sand:#ead3c3;
  --sage:#bccbbf;
  --barcode:#dcc3b5;
  --scene:#8b8d9e;
  --white:#ffffff;
  --soft-white:#f2efee;
  --line:#3a3a3a;
}
*{box-sizing:border-box;margin:0;padding:0}
html,body{width:1200px;height:3180px;overflow:hidden}
body{position:relative;background:var(--white);font-family:"Montserrat",sans-serif;color:var(--ink)}

/* ---------- Section 1: flat label ---------- */
.frame-band{position:absolute;left:0;top:0;width:1200px;height:1000px}
.label{position:absolute;left:115px;top:112px;width:970px;height:770px;overflow:hidden;
  background:
    radial-gradient(ellipse 140px 110px at 60px 60px,rgba(188,203,191,.85),transparent 70%),
    radial-gradient(ellipse 260px 200px at 860px 120px,rgba(221,228,231,1),transparent 75%),
    radial-gradient(ellipse 200px 260px at 900px 420px,rgba(221,228,231,.9),transparent 75%),
    radial-gradient(ellipse 200px 140px at 920px 560px,rgba(217,190,175,.7),transparent 70%),
    radial-gradient(ellipse 320px 160px at 150px 560px,rgba(234,211,195,.9),transparent 70%),
    var(--pink);
  box-shadow:0 3px 8px rgba(0,0,0,.25)}
.label-copy{position:absolute;left:57px;top:56px;width:215px;font-size:14.5px;line-height:18px;text-align:center}
.label-copy p{margin-bottom:16px}
.label-note{position:absolute;left:685px;top:524px;width:255px;font-size:14px;line-height:18px;text-align:center}
.label-bar{position:absolute;left:0;top:604px;width:100%;height:94px;background:var(--bar)}
.label-foot{position:absolute;left:0;top:698px;width:100%;height:72px;background:var(--sand)}

/* label front panel (reused for the bottle flat) */
.label-front{position:absolute;left:347px;top:0;width:275px;height:770px}
.label-front .tab{position:absolute;left:0;top:0;width:275px;height:160px;background:var(--ink);border-bottom-right-radius:34px}
.tagline{font-family:"Barlow Condensed",sans-serif;font-weight:400;color:var(--soft-white);text-align:center;letter-spacing:2px;white-space:nowrap}
.label-front .tagline{position:absolute;left:0;top:88px;width:275px;font-size:28px;line-height:32px}
.wordmark{font-family:"Barlow Condensed",sans-serif;font-weight:400;color:var(--ink);text-align:center;letter-spacing:3px}
.label-front .wordmark{position:absolute;left:0;top:190px;width:275px;font-size:80px;line-height:90px}
.product{font-family:"Barlow Condensed",sans-serif;font-weight:600;color:var(--ink)}
.label-front .product{position:absolute;left:3px;top:352px;font-size:52px;line-height:56px}
.benefit{font-family:"Barlow Condensed",sans-serif;font-weight:400;color:var(--ink)}
.label-front .benefit{position:absolute;left:3px;top:406px;font-size:33px;line-height:38px}
.actives{background:var(--ink);color:var(--soft-white);font-family:"Barlow Condensed",sans-serif;font-weight:400}
.label-front .actives{position:absolute;left:3px;top:452px;width:272px;height:76px;padding:6px 0 0 13px;font-size:25px;line-height:31px;border-radius:8px 0 60px 8px}
.skin{font-family:"Barlow Condensed",sans-serif;font-weight:400;color:var(--ink);white-space:nowrap}
.label-front .skin{position:absolute;left:3px;top:530px;font-size:25px;line-height:30px}
.label-front .bar-seg{position:absolute;left:0;top:604px;width:100%;height:94px;background:var(--bar)}
.volume{position:absolute;text-align:center;font-family:"Montserrat",sans-serif;color:var(--ink)}
.label-front .volume{left:0;top:717px;width:275px;font-size:21px}

/* icons */
.icon{position:absolute;display:flex;flex-direction:column;align-items:center;color:var(--soft-white);text-align:center}
.icon svg{display:block;fill:none;stroke:currentColor;stroke-width:1.8;stroke-linecap:round;stroke-linejoin:round}
.icon .ph{display:block;border:1.8px solid currentColor;border-radius:50%;background:rgba(255,255,255,.12)}
.icon b{font-family:"Montserrat",sans-serif;font-weight:600;display:block}
.icon-lg svg,.icon-lg .ph{width:42px;height:42px}
.icon-lg b{font-size:9px;line-height:10px;margin-top:7px}
.icon-sm svg,.icon-sm .ph{width:24px;height:24px}
.icon-sm b{font-size:5.5px;line-height:6.5px;margin-top:3px}

.barcode-slot{position:absolute;display:flex;align-items:center;justify-content:center;font-family:"Montserrat",sans-serif}
.label .barcode-slot{left:679px;top:622px;width:183px;height:95px;background:var(--ink);color:var(--soft-white);font-size:15px}

/* nutrition panel */
.nutrition{position:absolute;border:2px solid var(--line);background:var(--white);padding:.25em .45em .35em;font-family:"Libre Franklin",sans-serif;color:var(--line);line-height:1.25}
.nutrition h3{font-weight:800;font-size:2.15em;line-height:1.05;letter-spacing:-.01em}
.nutrition .servings{font-size:.95em}
.nutrition .size{display:flex;justify-content:space-between;font-weight:800;font-size:1.05em;border-bottom:.6em solid var(--line);padding-bottom:.1em}
.nutrition .aps{font-size:.55em;font-weight:800;margin-top:.3em}
.nutrition .cal{display:flex;justify-content:space-between;align-items:baseline;font-weight:800;border-bottom:.35em solid var(--line)}
.nutrition .cal span:first-child{font-size:1.6em}
.nutrition .cal span:last-child{font-size:2em}
.nutrition .dv{font-size:.55em;font-weight:800;text-align:right;padding:.2em 0;border-bottom:1px solid var(--line)}
.nutrition .row{display:flex;justify-content:space-between;font-size:.78em;padding:.12em 0;border-bottom:1px solid var(--line)}
.nutrition .row:last-child{border-bottom:0}
.nutrition .row strong{font-weight:800}
.nutrition .row em{font-style:italic}
.nutrition .in1{padding-left:1em}
.nutrition .in2{padding-left:2.2em}
.label .nutrition{left:670px;top:82px;width:275px;height:418px;font-size:12.6px}

/* ---------- Section 2: box dieline ---------- */
.dieline{position:absolute;left:0;top:0;width:1200px;height:2150px;pointer-events:none}
.panel{position:absolute;top:1177px;height:710px;overflow:hidden}
.panel-side-a{left:225px;width:204px;background:
  radial-gradient(ellipse 90px 80px at 40px 20px,rgba(188,203,191,.85),transparent 70%),
  radial-gradient(ellipse 160px 120px at 60px 560px,rgba(234,211,195,.9),transparent 70%),var(--pink)}
.panel-front{left:429px;width:203px;background:
  radial-gradient(ellipse 160px 140px at 150px 560px,rgba(234,211,195,.9),transparent 70%),var(--pink)}
.panel-side-b{left:632px;width:203px;background:
  radial-gradient(ellipse 110px 90px at 180px 60px,rgba(208,186,170,.7),transparent 70%),
  radial-gradient(ellipse 200px 200px at 100px 200px,var(--sky),transparent 75%),
  radial-gradient(ellipse 160px 140px at 60px 560px,rgba(234,211,195,.9),transparent 70%),var(--blush)}
.panel-back{left:835px;width:204px;background:
  radial-gradient(ellipse 120px 100px at 190px 420px,rgba(208,186,170,.75),transparent 70%),
  radial-gradient(ellipse 160px 120px at 60px 560px,rgba(234,211,195,.9),transparent 70%),var(--sky)}
.box-bar{position:absolute;left:225px;top:1775px;width:814px;height:50px;background:var(--bar)}
.box-foot{position:absolute;left:225px;top:1825px;width:814px;height:62px;background:var(--sand)}
.side-copy{position:absolute;left:19px;top:38px;width:168px;font-size:10.3px;line-height:12.9px;text-align:center}
.side-copy p{margin-bottom:12.5px}
.back-copy{position:absolute;left:17px;top:328px;width:170px;font-size:9.6px;line-height:11.6px;text-align:center}
.back-copy p{margin-bottom:9.5px}
.panel-side-b .nutrition{left:8px;top:36px;width:180px;height:268px;font-size:8.2px}

/* box front panel */
.box-front{position:absolute;left:0;top:0;width:203px;height:710px}
.box-front .tab{position:absolute;left:15px;top:0;width:175px;height:75px;background:var(--ink);border-bottom-right-radius:26px}
.box-front .tagline{position:absolute;left:15px;top:40px;width:175px;font-size:18px;line-height:22px;letter-spacing:1.5px}
.box-front .wordmark{position:absolute;left:0;top:158px;width:203px;font-size:56px;line-height:66px}
.box-front .product{position:absolute;left:22px;top:314px;font-size:29px;line-height:32px}
.box-front .benefit{position:absolute;left:22px;top:348px;font-size:29px;line-height:32px}
.box-front .actives{position:absolute;left:22px;top:425px;width:157px;height:72px;padding:3px 0 0 6px;font-size:20px;line-height:20px;border-radius:0 0 44px 0}
.box-front .skin{position:absolute;left:22px;top:505px;font-size:17px;line-height:21px}
.box-front .bar-seg{position:absolute;left:0;top:598px;width:100%;height:50px;background:var(--bar)}
.box-front .volume{left:0;top:661px;width:203px;font-size:12.5px}
.box-front .icon{top:604px}

/* ---------- Section 3: flat product set ---------- */
.set{position:absolute;left:0;top:2150px;width:1200px;height:1030px;background:var(--scene)}
.bottle-flat{position:absolute;left:0;top:0;width:275px;height:770px;transform-origin:0 0;
  background:
    radial-gradient(ellipse 180px 140px at 200px 720px,rgba(234,211,195,.95),transparent 70%),var(--pink);
  box-shadow:0 6px 18px rgba(0,0,0,.25)}
.bottle-flat .label-front{left:0}
.bottle-flat .foot{position:absolute;left:0;top:698px;width:100%;height:72px;background:var(--sand)}
.box-flat{position:absolute;width:203px;height:710px;overflow:hidden;background:
  radial-gradient(ellipse 160px 140px at 150px 560px,rgba(234,211,195,.9),transparent 70%),var(--pink);
  box-shadow:0 6px 18px rgba(0,0,0,.25)}
.box-flat .foot{position:absolute;left:0;top:648px;width:100%;height:62px;background:var(--sand)}
</style>
</head>
<body>

<svg width="0" height="0" style="position:absolute" aria-hidden="true">
  <defs>
    <symbol id="i-heart" viewBox="0 0 40 40"><path d="M20 34C9 25 4 19 6 12 8 6 16 5 20 12 24 5 32 6 34 12 36 19 31 25 20 34Z"/></symbol>
    <symbol id="i-leaf" viewBox="0 0 40 40"><path d="M20 33C13 27 13 18 20 10 27 18 27 27 20 33Z"/><path d="M20 33C12 34 5 30 3 21 11 20 17 25 20 33Z"/><path d="M20 33C28 34 35 30 37 21 29 20 23 25 20 33Z"/></symbol>
    <symbol id="i-recycle" viewBox="0 0 40 40"><path d="M15 11 20 4 25 11"/><path d="M17 8 9 22"/><path d="M31 18 33 27 25 29"/><path d="M23 8 31 22"/><path d="M14 36 7 30 14 24"/><path d="M10 30H30"/></symbol>
    <symbol id="i-jar" viewBox="0 0 40 40"><path d="M9 16H31V34H9Z"/><path d="M8 11H32V16"/><path d="M8 11 12 5"/><text x="20" y="29" text-anchor="middle" font-family="Montserrat, sans-serif" font-size="9" font-weight="600" fill="currentColor" stroke="none">6 M</text></symbol>
  </defs>
</svg>

<!-- ========== Section 1: label ========== -->
<svg class="frame-band" viewBox="0 0 1200 1000" aria-hidden="true">
  <polygon points="100,0 1200,0 1200,1000 1085,882 1085,112 212,112" fill="#646566"/>
</svg>

<section class="label" aria-label="Three-panel bottle label">
  <div class="label-copy">
    <p>Lorem ipsum dolor sit amet, consectetuer adipiscing elit, sed diam nonummy nibh euismod tincidunt ut laoreet dolore magna aliquam erat volutpat.</p>
    <p>Lorem ipsum dolor sit amet, consectetuer adipiscing elit, sed diam nonummy nibh euismod tincidunt ut laoreet dolore magna aliquam erat volutpat.</p>
    <p>Lorem ipsum dolor sit amet, consectetuer adipiscing elit, sed diam nonummy nibh euismod tincidunt ut laoreet dolore magna aliquam erat volutpat.</p>
    <p>Lorem ipsum dolor sit amet, consectetuer adipiscing elit, sed diam nonummy nibh euismod tincidunt ut laoreet dolore magna aliquam erat volutpat.</p>
  </div>

  <div class="nutrition">
    <h3>Nutrition Facts</h3>
    <div class="servings">10 servings per container</div>
    <div class="size"><span>Serving size</span><span>1 cup (55g)</span></div>
    <div class="aps">Amount per serving</div>
    <div class="cal"><span>Calories</span><span>165</span></div>
    <div class="dv">% Daily Value*</div>
    <div class="row"><span><strong>Total Fat</strong> 1.5g</span><strong>2%</strong></div>
    <div class="row in1"><span>Saturated Fat 0.5g</span><strong>3%</strong></div>
    <div class="row in1"><span><em>Trans</em> Fat 0g</span></div>
    <div class="row in1"><span>Polyunsaturated Fat 0.5g</span></div>
    <div class="row in1"><span>Monounsaturated Fat 0.5g</span></div>
    <div class="row"><span><strong>Cholesterol</strong> 0mg</span><strong>0%</strong></div>
    <div class="row"><span><strong>Sodium</strong> 180mg</span><strong>8%</strong></div>
    <div class="row"><span><strong>Fluoride</strong> 0g</span></div>
    <div class="row"><span><strong>Total Carbohydrate</strong> 21g</span><strong>8%</strong></div>
    <div class="row in1"><span>Dietary Fiber 2g</span><strong>7%</strong></div>
    <div class="row in2"><span>Soluble Fiber &lt;1g</span></div>
    <div class="row in2"><span>Insoluble Fiber 1g</span></div>
    <div class="row in1"><span>Total Sugars 8g</span></div>
  </div>
  <p class="label-note">Lorem ipsum dolor sit amet, consectetuer adipiscing elit, sed diam nonummy nibh euismod tincidunt ut laoreet volutpat.</p>

  <div class="label-bar"></div>
  <div class="label-foot"></div>

  <div class="icon icon-lg" style="left:62px;top:622px;width:46px"><svg viewBox="0 0 40 40"><use href="#i-recycle"/></svg><b>Please<br>Recycle</b></div>
  <div class="icon icon-lg" style="left:124px;top:622px;width:76px"><span class="ph" role="img" aria-label="Ethical and sustainable globe icon"></span><b>Ethical &amp;<br>Sustainable</b></div>
  <div class="icon icon-lg" style="left:206px;top:622px;width:60px"><span class="ph" role="img" aria-label="Cruelty free rabbit icon"></span><b>Cruelty<br>Free</b></div>

  <div class="label-front">
    <div class="tab"></div>
    <div class="tagline">pure by design</div>
    <div class="wordmark">Quenra</div>
    <div class="product">MOISTURISER</div>
    <div class="benefit">Hydrate &amp; Nourish</div>
    <div class="actives">Hyaluronic Acid<br>Desert Lime &amp; Green Tea.</div>
    <div class="skin">All Skin Types Dry - Dehydrated</div>
    <div class="bar-seg"></div>
    <div class="icon icon-lg" style="left:17px;top:622px;width:50px"><svg viewBox="0 0 40 40"><use href="#i-heart"/></svg><b>100%<br>Vegan</b></div>
    <div class="icon icon-lg" style="left:98px;top:622px;width:80px"><span class="ph" role="img" aria-label="Product of Australia kangaroo icon"></span><b>Product of<br>Australia</b></div>
    <div class="icon icon-lg" style="left:213px;top:622px;width:50px"><svg viewBox="0 0 40 40"><use href="#i-leaf"/></svg><b>100%<br>Natural</b></div>
    <div class="volume">60mL</div>
  </div>

  <div class="barcode-slot">bar code</div>
  <div class="icon icon-lg" style="left:880px;top:614px;width:60px"><svg viewBox="0 0 40 40" style="width:34px;height:34px"><use href="#i-jar"/></svg><b>6 Months<br>Once Open</b></div>
</section>

<!-- ========== Section 2: box dieline ========== -->
<div class="panel panel-side-a">
  <div class="side-copy">
    <p>Lorem ipsum dolor sit amet, consectetuer adipiscing elit, sed diam nonummy nibh euismod tincidunt ut laoreet dolore magna aliquam erat volutpat.</p>
    <p>Lorem ipsum dolor sit amet, consectetuer adipiscing elit, sed diam nonummy nibh euismod tincidunt ut laoreet dolore magna aliquam erat volutpat.</p>
    <p>Lorem ipsum dolor sit amet, consectetuer adipiscing elit, sed diam nonummy nibh euismod tincidunt ut laoreet dolore magna aliquam erat volutpat.</p>
    <p>Lorem ipsum dolor sit amet, consectetuer adipiscing elit, sed diam nonummy nibh euismod tincidunt ut laoreet dolore magna aliquam erat volutpat.</p>
    <p>Lorem ipsum dolor sit amet, consectetuer adipiscing elit, sed diam nonummy nibh euismod tincidunt ut laoreet dolore magna aliquam erat volutpat.</p>
    <p>Lorem ipsum dolor sit amet, consectetuer adipiscing elit, sed diam nonummy nibh euismod tincidunt ut laoreet dolore magna aliquam erat volutpat.</p>
  </div>
</div>

<div class="panel panel-front">
  <div class="box-front">
    <div class="tab"></div>
    <div class="tagline">pure by design</div>
    <div class="wordmark">Quenra</div>
    <div class="product">MOISTURISER</div>
    <div class="benefit">Hydrate<br>&amp; Nourish</div>
    <div class="actives">Hyaluronic Acid<br>Desert Lime &amp;<br>Green Tea.</div>
    <div class="skin">All Skin Types<br>Dry - Dehydrated</div>
  </div>
</div>

<div class="panel panel-side-b">
  <div class="nutrition">
    <h3>Nutrition Facts</h3>
    <div class="servings">10 servings per container</div>
    <div class="size"><span>Serving size</span><span>1 cup (55g)</span></div>
    <div class="aps">Amount per serving</div>
    <div class="cal"><span>Calories</span><span>165</span></div>
    <div class="dv">% Daily Value*</div>
    <div class="row"><span><strong>Total Fat</strong> 1.5g</span><strong>2%</strong></div>
    <div class="row in1"><span>Saturated Fat 0.5g</span><strong>3%</strong></div>
    <div class="row in1"><span><em>Trans</em> Fat 0g</span></div>
    <div class="row in1"><span>Polyunsaturated Fat 0.5g</span></div>
    <div class="row in1"><span>Monounsaturated Fat 0.5g</span></div>
    <div class="row"><span><strong>Cholesterol</strong> 0mg</span><strong>0%</strong></div>
    <div class="row"><span><strong>Sodium</strong> 180mg</span><strong>8%</strong></div>
    <div class="row"><span><strong>Fluoride</strong> 0g</span></div>
    <div class="row"><span><strong>Total Carbohydrate</strong> 21g</span><strong>8%</strong></div>
    <div class="row in1"><span>Dietary Fiber 2g</span><strong>7%</strong></div>
    <div class="row in2"><span>Soluble Fiber &lt;1g</span></div>
    <div class="row in2"><span>Insoluble Fiber 1g</span></div>
    <div class="row in1"><span>Total Sugars 8g</span></div>
  </div>
  <div class="back-copy">
    <p>Lorem ipsum dolor sit amet, consectetuer adipiscing elit, sed diam nonummy nibh euismod tincidunt ut laoreet dolore magna aliquam erat volutpat.</p>
    <p>Lorem ipsum dolor sit amet, consectetuer adipiscing elit, sed diam nonummy nibh euismod tincidunt ut laoreet dolore magna aliquam erat volutpat.</p>
    <p>Lorem ipsum dolor sit amet, consectetuer adipiscing elit, sed diam nonummy nibh euismod tincidunt ut laoreet dolore magna aliquam erat volutpat.</p>
    <p>Lorem ipsum dolor sit amet, consectetuer adipiscing elit, sed diam nonummy nibh euismod tincidunt ut laoreet dolore magna aliquam erat volutpat.</p>
  </div>
</div>

<div class="panel panel-back">
  <div class="box-front">
    <div class="tab"></div>
    <div class="tagline">pure by design</div>
    <div class="wordmark">Quenra</div>
    <div class="product">MOISTURISER</div>
    <div class="benefit">Hydrate<br>&amp; Nourish</div>
    <div class="actives">Hyaluronic Acid<br>Desert Lime &amp;<br>Green Tea.</div>
    <div class="skin">All Skin Types<br>Dry - Dehydrated</div>
  </div>
</div>

<div class="box-bar"></div>
<div class="box-foot"></div>

<!-- wrap-around icon bar contents -->
<div class="icon icon-sm" style="left:263px;top:1782px;width:40px"><svg viewBox="0 0 40 40"><use href="#i-recycle"/></svg><b>Please<br>Recycle</b></div>
<div class="icon icon-sm" style="left:300px;top:1782px;width:48px"><span class="ph" role="img" aria-label="Ethical and sustainable globe icon"></span><b>Ethical &amp;<br>Sustainable</b></div>
<div class="icon icon-sm" style="left:345px;top:1782px;width:40px"><span class="ph" role="img" aria-label="Cruelty free rabbit icon"></span><b>Cruelty<br>Free</b></div>

<div class="icon icon-sm" style="left:449px;top:1782px;width:40px"><svg viewBox="0 0 40 40"><use href="#i-heart"/></svg><b>100%<br>Vegan</b></div>
<div class="icon icon-sm" style="left:505px;top:1782px;width:50px"><span class="ph" role="img" aria-label="Product of Australia kangaroo icon"></span><b>Product of<br>Australia</b></div>
<div class="icon icon-sm" style="left:568px;top:1782px;width:40px"><svg viewBox="0 0 40 40"><use href="#i-leaf"/></svg><b>100%<br>Natural</b></div>
<div class="volume" style="left:429px;top:1838px;width:203px;font-size:12.5px">60mL</div>

<div class="icon icon-sm" style="left:765px;top:1780px;width:50px"><svg viewBox="0 0 40 40"><use href="#i-jar"/></svg><b>6 Months<br>Once Open</b></div>
<div class="barcode-slot" style="left:649px;top:1796px;width:115px;height:48px;background:var(--barcode);color:var(--ink);font-size:14px">bar code</div>

<div class="icon icon-sm" style="left:855px;top:1782px;width:40px"><svg viewBox="0 0 40 40"><use href="#i-heart"/></svg><b>100%<br>Vegan</b></div>
<div class="icon icon-sm" style="left:911px;top:1782px;width:50px"><span class="ph" role="img" aria-label="Product of Australia kangaroo icon"></span><b>Product of<br>Australia</b></div>
<div class="icon icon-sm" style="left:974px;top:1782px;width:40px"><svg viewBox="0 0 40 40"><use href="#i-leaf"/></svg><b>100%<br>Natural</b></div>
<div class="volume" style="left:835px;top:1838px;width:204px;font-size:12.5px">60mL</div>

<svg class="dieline" viewBox="0 0 1200 2150" aria-hidden="true">
  <g fill="none" stroke="#1a1a1a" stroke-width="1.4">
    <rect x="225" y="1177" width="814" height="710"/>
    <path d="M429 1177V1887M632 1177V1887M835 1177V1887"/>
    <path d="M225 1195L160 1212V1868L225 1885"/>
    <path d="M225 1177L235 1150V1060H402V1150L429 1177"/>
    <path d="M632 1177L660 1150V1060H825V1150L835 1177"/>
    <path d="M835 1177V1040L838 1035V975Q838 950 863 950H1011Q1036 950 1036 975V1035L1039 1040V1177M835 1040H1039"/>
    <path d="M225 1887L235 1915V2000H402V1915L429 1887"/>
    <path d="M429 1887V2052L432 2057V2087Q432 2112 457 2112H604Q629 2112 629 2087V2057L632 2052V1887M429 2052H632"/>
    <path d="M632 1887L660 1915V2000H825V1915L835 1887"/>
  </g>
</svg>

<!-- ========== Section 3: flat bottle label and box front ========== -->
<section class="set" aria-label="Bottle label and box front">
  <div class="bottle-flat" style="left:360px;top:250px;transform:scale(.78)">
    <div class="foot"></div>
    <div class="label-front">
      <div class="tab"></div>
      <div class="tagline">pure by design</div>
      <div class="wordmark">Quenra</div>
      <div class="product">MOISTURISER</div>
      <div class="benefit">Hydrate &amp; Nourish</div>
      <div class="actives">Hyaluronic Acid<br>Desert Lime &amp; Green Tea.</div>
      <div class="skin">All Skin Types Dry - Dehydrated</div>
      <div class="bar-seg"></div>
      <div class="icon icon-lg" style="left:17px;top:622px;width:50px"><svg viewBox="0 0 40 40"><use href="#i-heart"/></svg><b>100%<br>Vegan</b></div>
      <div class="icon icon-lg" style="left:98px;top:622px;width:80px"><span class="ph" role="img" aria-label="Product of Australia kangaroo icon"></span><b>Product of<br>Australia</b></div>
      <div class="icon icon-lg" style="left:213px;top:622px;width:50px"><svg viewBox="0 0 40 40"><use href="#i-leaf"/></svg><b>100%<br>Natural</b></div>
      <div class="volume">60mL</div>
    </div>
  </div>

  <div class="box-flat" style="left:632px;top:160px">
    <div class="foot"></div>
    <div class="box-front">
      <div class="tab"></div>
      <div class="tagline">pure by design</div>
      <div class="wordmark">Quenra</div>
      <div class="product">MOISTURISER</div>
      <div class="benefit">Hydrate<br>&amp; Nourish</div>
      <div class="actives">Hyaluronic Acid<br>Desert Lime &amp;<br>Green Tea.</div>
      <div class="skin">All Skin Types<br>Dry - Dehydrated</div>
      <div class="bar-seg"></div>
      <div class="icon icon-sm" style="left:20px;width:40px"><svg viewBox="0 0 40 40"><use href="#i-heart"/></svg><b>100%<br>Vegan</b></div>
      <div class="icon icon-sm" style="left:76px;width:50px"><span class="ph" role="img" aria-label="Product of Australia kangaroo icon"></span><b>Product of<br>Australia</b></div>
      <div class="icon icon-sm" style="left:139px;width:40px"><svg viewBox="0 0 40 40"><use href="#i-leaf"/></svg><b>100%<br>Natural</b></div>
      <div class="volume">60mL</div>
    </div>
  </div>
</section>

</body>
</html>
```